Stationary for Non-Profit Ministry
Jared & Lydia Ministries
Professional
Jared Pelowski
Speaker
4817 W. Harrow Lane Ozark, MO 65894
jaredpl47@mailora.net
www.jared-lydia.org
creatively arranged logo

```html
<!DOCTYPE html>
<html lang="en">
<head>
<meta charset="utf-8">
<title>Jared &amp; Lydia Ministries – Business Card</title>
<link rel="stylesheet" href="https://fonts.googleapis.com/css2?family=Tinos:wght@400&display=swap">
<style>
  :root {
    --backdrop-light: #f2f2f2;
    --backdrop-dark: #cdcdcd;
    --card: #ffffff;
    --green: #4e8a1f;
    --green-dark: #2c5410;
    --green-light: #8cc63f;
    --red: #c8281c;
    --ink: #2b2b2b;
  }
  * { box-sizing: border-box; margin: 0; padding: 0; }
  html, body { width: 1200px; height: 945px; overflow: hidden; }
  body {
    background: radial-gradient(ellipse at center, var(--backdrop-light) 0%, var(--backdrop-dark) 100%);
    font-family: "Tinos", "Times New Roman", serif;
    position: relative;
  }
  .card {
    position: absolute;
    left: 259px;
    width: 670px;
    height: 376px;
    background: var(--card);
    box-shadow: 0 3px 10px rgba(0,0,0,0.25);
    overflow: hidden;
  }
  .card--front { top: 77px; }
  .card--back { top: 507px; }

  .edge-tab {
    position: absolute;
    width: 20px;
    background: linear-gradient(90deg, var(--green-light), var(--green));
  }
  .card--front .edge-tab { top: 56px; height: 277px; }
  .card--back .edge-tab { top: 61px; height: 260px; }
  .edge-tab--right { right: 0; border-radius: 14px 0 0 14px; }
  .edge-tab--left { left: 0; border-radius: 0 14px 14px 0; background: linear-gradient(270deg, var(--green-light), var(--green)); }

  .brand-dot {
    position: absolute;
    border-radius: 50%;
    background: var(--green);
  }
  .card--front .brand-dot { left: 32px; top: 110px; width: 90px; height: 90px; }
  .brand-name--vertical {
    position: absolute;
    left: 156px;
    top: 16px;
    transform-origin: 0 0;
    transform: rotate(90deg);
    font-size: 24px;
    line-height: 30px;
    color: var(--red);
    white-space: nowrap;
  }

  .name-bar {
    position: absolute;
    left: 345px;
    top: 130px;
    width: 325px;
    height: 50px;
    background: linear-gradient(90deg, var(--green-dark), var(--green));
    color: #fff;
    font-size: 34px;
    line-height: 50px;
    padding-left: 14px;
    white-space: nowrap;
  }
  .role {
    position: absolute;
    right: 70px;
    top: 190px;
    font-size: 18px;
    color: var(--ink);
  }
  .contact {
    position: absolute;
    right: 42px;
    top: 264px;
    text-align: right;
    font-size: 15px;
    line-height: 28px;
    color: var(--ink);
    white-space: nowrap;
  }

  .card--back .brand-dot { left: 275px; top: 44px; width: 120px; height: 120px; }
  .brand-name {
    position: absolute;
    left: 0;
    right: 0;
    top: 200px;
    text-align: center;
    font-size: 40px;
    color: var(--red);
    white-space: nowrap;
  }
  .web-band {
    position: absolute;
    left: 0;
    right: 0;
    bottom: 0;
    height: 56px;
    background: linear-gradient(90deg, var(--green-light), var(--green) 30%, var(--green-dark));
    border-radius: 28px 0 0 0;
    color: #fff;
    font-size: 20px;
    text-align: center;
    line-height: 56px;
  }
</style>
</head>
<body>
  <section class="card card--front" aria-label="Business card front">
    <div class="brand-dot"></div>
    <div class="brand-name--vertical">Jared &amp; Lydia Ministries</div>
    <div class="name-bar">Jared Pelowski</div>
    <div class="role">Speaker</div>
    <div class="contact">
      <p>E-mail: jaredpl47@mailora.net</p>
      <p>Tool Free # 800-555-0148 &nbsp;|&nbsp; Cell # 417-555-0193</p>
      <p>Address: 4817 W. Harrow Lane, Ozark, MO 65894</p>
      <p>Web: www.jared-lydia.org</p>
    </div>
    <div class="edge-tab edge-tab--right"></div>
  </section>

  <section class="card card--back" aria-label="Business card back">
    <div class="edge-tab edge-tab--left"></div>
    <div class="edge-tab edge-tab--right"></div>
    <div class="brand-dot"></div>
    <div class="brand-name">Jared &amp; Lydia Ministries</div>
    <div class="web-band">www.jared-lydia.org</div>
  </section>
</body>
</html>
```